velmorique hair oil

Its an ayurvedic hair oil of 100 ml bottle. We need a design for the label. along with the wordings, some punch line too in the label. Mettalic silver bottle with black cap. Round bottle with height of 10 cm and width of 7 cm. The metallic silver colour bottle can be changed if some other nice colour combination is worked out

Reason: Had to design the bottle size and hence we have more time now

Target Market(s)

Retail, any one with a hair fall problem can be our target customer.. This ayurvedic hair oil is a miracle off sorts. With just one bottle hair fall totally stops and fresh hair grows.

Industry/Entity Type

Hair

Requirements
Must have
• HAVE WORDS 100% AYURVEDIC HAIR OIL IN A CIRCLE

MUST NOTE THAT THE BOTTLE IS ROUND
Nice to have
• Its for both men and women. Bottle is round in shape and hence the wording should be accordingly put
Should not have
• RED COLOUR.

```html
<!DOCTYPE html>
<html lang="en">
<head>
<meta charset="utf-8">
<title>velmorique hair oil label</title>
<link rel="stylesheet" href="https://fonts.googleapis.com/css2?family=Hind:wght@400;500;600&family=Archivo+Narrow:wght@400;500&display=swap">
<style>
  :root {
    --canvas: #ffffff;
    --label-bg: #ffffff;
    --label-edge: #e4e4e4;
    --ink: #231f20;
    --ink-soft: #3a3a3a;
    --rule: #2b2b2b;
    --panel: #231f20;
    --brand-yellow: #fff200;
    --gold-light: #f3e3a6;
    --gold: #c9a34a;
    --gold-deep: #8f6a25;
  }
  * { margin: 0; padding: 0; box-sizing: border-box; }
  html, body {
    width: 1200px;
    height: 1000px;
    overflow: hidden;
    background: var(--canvas);
  }
  .canvas {
    position: relative;
    width: 1200px;
    height: 1000px;
  }
  .label {
    position: absolute;
    left: 50px;
    top: 223px;
    width: 688px;
    height: 346px;
    background: var(--label-bg);
    border: 3px solid var(--label-edge);
    transform: scale(1.6);
    transform-origin: top left;
    font-family: "Hind", sans-serif;
    color: var(--ink);
  }
  .brand-panel {
    position: absolute;
    display: flex;
    flex-direction: column;
  }
  .brand-panel--back { left: 29px; top: 16px; width: 126px; height: 109px; }
  .brand-panel--front { left: 460px; top: -3px; width: 160px; height: 148px; }
  .brand-block {
    flex: 1;
    background: var(--panel);
    display: flex;
    align-items: center;
    justify-content: center;
  }
  .brand-name {
    font-family: "Hind", sans-serif;
    font-weight: 600;
    color: var(--brand-yellow);
    letter-spacing: 0.2px;
    line-height: 1;
    padding-top: 4px;
  }
  .brand-panel--back .brand-name { font-size: 21px; }
  .brand-panel--front .brand-name { font-size: 27px; }
  .gold-wave {
    background: linear-gradient(180deg, var(--panel) 0%, var(--gold-deep) 30%, var(--gold-light) 55%, var(--gold) 75%, #ffffff 100%);
  }
  .brand-panel--back .gold-wave { height: 26px; }
  .brand-panel--front .gold-wave { height: 32px; }
  .ingredients {
    position: absolute;
    left: 28px;
    top: 138px;
    width: 212px;
    font-family: "Archivo Narrow", sans-serif;
    font-size: 11.4px;
    line-height: 15.6px;
    color: var(--ink);
  }
  .ingredients strong { font-weight: 500; }
  .distributor {
    position: absolute;
    left: 25px;
    top: 279px;
    font-size: 14px;
    color: var(--ink-soft);
  }
  .website {
    position: absolute;
    left: 25px;
    width: 245px;
    top: 299px;
    text-align: center;
    font-size: 14px;
    color: var(--ink-soft);
  }
  .front-panel {
    position: absolute;
    left: 460px;
    top: 168px;
    width: 160px;
    text-align: center;
  }
  .product-name {
    font-size: 14.5px;
    line-height: 18px;
    letter-spacing: 0.2px;
    color: var(--ink-soft);
  }
  .product-rule {
    height: 1.5px;
    background: var(--rule);
    margin: 4px 0 9px;
  }
  .tagline {
    font-size: 11px;
    color: var(--ink);
  }
  .volume {
    margin-top: 44px;
    font-size: 14px;
    color: var(--ink-soft);
  }
</style>
</head>
<body>
<div class="canvas">
  <section class="label">
    <div class="brand-panel brand-panel--back">
      <div class="brand-block"><span class="brand-name">velmorique</span></div>
      <div class="gold-wave" role="img" aria-label="Gold wave ornament"></div>
    </div>
    <p class="ingredients"><strong>INGREDIENTS:</strong>Lorem ipsum dolor sit amet, consectetuer adipiscing elit, sed diam nonummy nibh euismod tincidunt ut laoreet dolore magna aliquam erat volutpat. Ut wisi enim ad minim veniam, quis nostrud exerci tation ullamcorper suscipit lobortis nisl ut aliquip ex ea commodo consequat.</p>
    <p class="distributor">Distruted By: Name of the company</p>
    <p class="website">www.velmoriqueherbs.com</p>

    <div class="brand-panel brand-panel--front">
      <div class="brand-block"><span class="brand-name">velmorique</span></div>
      <div class="gold-wave" role="img" aria-label="Gold wave ornament"></div>
    </div>
    <div class="front-panel">
      <p class="product-name">100% AYURVEDIC<br>PREMIUM HAIR OIL</p>
      <div class="product-rule"></div>
      <p class="tagline">Fastest way to stop hair fall</p>
      <p class="volume">100 mL</p>
    </div>
  </section>
</div>
</body>
</html>
```